Coconut oil Product for Private Label Creation

We need a product label design for coconut oil.
We will provide you with all the related information(nutrition fact, brand logo, description)
My brand name is Tidewell Pantry and I attached brand logo.
I attached the good example for other products.
In the front, I focus on the freshness of the product on the white background.
We make the real image of coconut in half.
In the back side, we describe the story of the producer and products with his name and signature. In additions, the company name and address, website, Product of Mexico ... etc.

Target Market(s)

20-30 year old lady

Industry/Entity Type

Nutrition

Colors
add136
33a6d7

Requirements
Must have
• 1. Brand Name and logo : Tidewell Pantry
• 2. Certification : QRLB, KOSHER, NON-GMO
• 3. Sentence : 100% fresh organic extra virgin coconut oil - in the front upper
• unrefined, Cold-Pressed, Gluten-Free - in the front bottom
• 4. We prefer to image design the real fresh coconut in half - in the middle front
• Farm to the table icon
• 5. We will describe the story for producer and product - in the back side A
• 6. We will describe the nutrition fact, ingredients, company information, web-site, bar-code in the back side B
Nice to have
• I attached the good example.
• I attached the bottle shape & size. the circumference of bottle : 27 cm,
• the height of the label : 6cm, the diameter of the cap : 6.7cm, capacity : 500ml

```html
<!DOCTYPE html>
<html lang="en">
<head>
<meta charset="UTF-8">
<title>Tidewell Pantry Coconut Oil Label</title>
<link href="https://fonts.googleapis.com/css2?family=Mulish:wght@300;400;700;800&display=swap" rel="stylesheet">
<style>
  :root {
    --lime: #add136;
    --lime-text: #9cc231;
    --blue: #33a6d7;
    --brand-dark: #3b2620;
    --rule: #b9d46a;
    --frame: #b8b8b8;
    --white: #ffffff;
    --palm-a: #5fa83a;
    --palm-b: #cfe6b8;
    --photo-brown: #a87a52;
    --photo-cream: #efe9df;
    --photo-green: #6fae4a;
  }
  * { margin: 0; padding: 0; box-sizing: border-box; }
  html, body {
    width: 1200px; height: 1000px; overflow: hidden;
    background: var(--white);
    font-family: "Mulish", Arial, sans-serif;
  }
  .label {
    position: absolute; left: 100px; top: 212px;
    width: 1000px; height: 576px;
    border: 1px solid var(--frame);
    background: var(--white);
    overflow: hidden;
  }
  .palm {
    position: absolute; top: 0; height: 100px;
    background: linear-gradient(180deg, var(--palm-a) 0%, var(--palm-b) 70%, rgba(255,255,255,0) 100%);
  }
  .palm--left { left: 0; width: 306px; border-bottom-right-radius: 60% 100%; }
  .palm--right { right: 0; width: 298px; border-bottom-left-radius: 60% 100%; }
  .brand {
    position: absolute; left: 0; right: 0; top: 34px;
    display: flex; justify-content: center; align-items: center; gap: 12px;
  }
  .brand__mark { width: 18px; height: 18px; border-radius: 50%; background: var(--lime); }
  .brand__name {
    font-weight: 800; font-size: 40px; color: var(--brand-dark);
    letter-spacing: 0.01em; line-height: 1;
  }
  .brand__rule {
    position: absolute; left: 298px; width: 408px; top: 87px;
    height: 5px; background: var(--lime); border-radius: 3px;
  }
  .ruled {
    position: absolute; left: 0; right: 0;
    display: flex; justify-content: center; align-items: center;
    color: var(--lime-text); font-weight: 400; line-height: 1;
  }
  .ruled::before, .ruled::after { content: ""; height: 1.5px; background: var(--rule); }
  .tagline { top: 113px; font-size: 24px; gap: 14px; }
  .tagline::before, .tagline::after { width: 30px; }
  .certified { top: 217px; font-size: 24px; gap: 18px; }
  .certified::before, .certified::after { width: 90px; }
  .product-name {
    position: absolute; left: 0; right: 0; top: 146px;
    text-align: center; font-size: 52px; line-height: 1;
    color: var(--lime); letter-spacing: 0.2em;
  }
  .product-name__main { font-weight: 800; }
  .product-name__sub { font-weight: 300; }
  .coconut-photo {
    position: absolute; left: 218px; top: 272px; width: 573px; height: 290px;
    background: linear-gradient(170deg, var(--photo-brown) 0%, var(--photo-cream) 50%, var(--photo-green) 100%);
    border-radius: 48% 48% 12% 12% / 60% 60% 12% 12%;
    opacity: 0.85;
  }
  .claims {
    position: absolute; left: 282px; top: 542px; width: 447px; height: 33px;
    background: var(--blue); color: var(--white);
    font-size: 22px; font-weight: 400; line-height: 1;
    display: flex; align-items: center; justify-content: center;
    z-index: 2;
  }
</style>
</head>
<body>
  <main class="label">
    <div class="palm palm--left" role="img" aria-label="Palm fronds hanging into the top left corner"></div>
    <div class="palm palm--right" role="img" aria-label="Palm fronds hanging into the top right corner"></div>

    <div class="brand">
      <span class="brand__name">Tidewell Pantry</span>
      <span class="brand__mark"></span>
    </div>
    <div class="brand__rule"></div>

    <p class="ruled tagline">100% fresh organic extra virgin</p>
    <h1 class="product-name"><span class="product-name__main">COCONUT</span><span class="product-name__sub">OIL</span></h1>
    <p class="ruled certified">Organically Certified</p>

    <div class="coconut-photo" role="img" aria-label="Photo of fresh coconuts, one whole and two split in half showing white flesh, resting on green leaves"></div>
    <div class="claims">Cold Pressed - Gluten Free</div>
  </main>
</body>
</html>
```